Redesign Of Flower Delivery Subscription Service Website

I need a revamped website of www.petal-tide.com

Please revamp current design using same content....

Target Market(s)

people who buy flowers. Brides, wedding planners, wedding photographer, married man, boyfriend, etc.

Industry/Entity Type

Florist

Number of Pages Required

5+ page

Colors

Designer to choose colors to be used in the design.

Requirements
Must have
• I need a revamped website of www.petal-tide.com
• Please revamp current design using same content....
Nice to have
Should not have

```html
<!DOCTYPE html>
<html lang="en">
<head>
<meta charset="utf-8">
<title>PetalTide – Monthly Flower Delivery</title>
<link href="https://fonts.googleapis.com/css2?family=Great+Vibes&family=Montserrat:wght@400;600;700&family=Lora:ital,wght@0,400;1,400;1,700&family=Playfair+Display:ital,wght@1,700&display=swap" rel="stylesheet">
<style>
:root{
  --green:#8cc63f;
  --green-dark:#2c3b12;
  --gold:#d6ab55;
  --gold-light:#e7c98c;
  --ink:#333333;
  --muted:#6b6b6b;
  --line:#9a9a9a;
  --paper:#ffffff;
  --cream:#fbf6ee;
  --banner:#dfe2e3;
  --video:#2a2d33;
  --footer-text:#ffffff;
  --footer-line:#7a8566;
}
*{box-sizing:border-box;margin:0;padding:0}
html,body{width:1200px;height:3488px;overflow:hidden;background:var(--paper)}
body{position:relative;font-family:"Lora",Georgia,serif;color:var(--ink)}
.abs{position:absolute}
.caps{font-family:"Montserrat",Arial,sans-serif;text-transform:uppercase}

/* header */
.site-header{left:0;top:0;width:1200px;height:93px;background:var(--paper);border-bottom:1px solid #eee}
.nav{top:40px;font-size:9.5px;font-weight:600;color:#444;letter-spacing:.2px;white-space:nowrap}
.brand{left:490px;top:16px;width:220px;text-align:center;font-family:"Montserrat",Arial,sans-serif;font-size:30px;font-weight:600;color:var(--green);letter-spacing:1px}
.brand small{display:block;font-size:9px;letter-spacing:1px;color:#888;font-weight:400;margin-top:-2px}

/* hero */
.hero{left:0;top:93px;width:1200px;height:519px;background:linear-gradient(100deg,#a9a6a0 0%,#c8c3bd 35%,#b77d8e 60%,#9d2e48 85%,#6f7c4d 100%)}
.hero-title{left:150px;top:170px;font-family:"Great Vibes",cursive;font-size:168px;color:#fff;line-height:1;white-space:nowrap}
.hero-sub{left:165px;top:425px;font-family:"Lora",serif;font-style:italic;font-weight:700;font-size:21px;color:#fff;white-space:nowrap}
.hero-price{left:198px;top:462px;font-family:"Lora",serif;font-style:italic;font-weight:700;font-size:21px;color:#fff;white-space:nowrap}
.hero-price b{color:#f2dc3a;font-size:30px}

/* perks */
.perk{top:647px;width:247px;height:102px;border:2px dashed #9a9a9a;text-align:center;padding-top:18px}
.perk .note{font-size:10px;color:var(--muted);font-family:"Montserrat",sans-serif}
.perk .name{font-family:"Montserrat",sans-serif;font-weight:700;font-size:17px;letter-spacing:1.5px;margin-top:4px}
.perk .more{font-size:9px;color:var(--gold);font-family:"Montserrat",sans-serif;margin-top:6px}

/* cards */
.card{top:791px;height:367px;background:var(--cream)}
.card .photo{position:absolute;left:0;top:0;width:100%;height:291px}
.card .label{position:absolute;left:0;bottom:22px;width:100%;text-align:center;font-family:"Montserrat",sans-serif;font-weight:600;font-size:15px;color:var(--gold);letter-spacing:1px}
.card-feature{background:#fff;box-shadow:0 4px 16px rgba(0,0,0,.22)}
.card-feature .photo{left:14px;top:12px;width:309px;height:240px}
.card-feature .over{position:absolute;left:14px;top:110px;width:309px;text-align:center;color:#fff;font-family:"Montserrat",sans-serif;font-weight:700;font-size:15px}
.card-feature p{position:absolute;left:18px;top:258px;width:301px;text-align:center;font-family:"Montserrat",sans-serif;font-size:11.5px;line-height:1.6;color:#444}

/* signup + video */
.signup{left:135px;top:1262px;width:400px}
.signup h3{font-family:"Montserrat",sans-serif;font-weight:600;font-size:13px;letter-spacing:.5px}
.signup p{font-size:12px;color:var(--muted);line-height:1.65;margin-top:22px}
.signup .field{margin-top:26px;height:40px;border:1px dashed #aaa;font-size:10px;color:#aaa;padding:12px 14px}
.signup .btn{margin-top:24px;width:116px;height:40px;border-radius:20px;background:var(--green);color:#fff;font-family:"Montserrat",sans-serif;font-weight:700;font-size:10px;text-align:center;line-height:40px}
.signup .fine{margin-top:30px;font-size:9px;color:#999;font-style:italic}
.video{left:600px;top:1205px;width:544px;height:423px;background:var(--video)}

/* intro */
.intro-title{left:0;top:1712px;width:1200px;text-align:center;font-family:"Playfair Display",serif;font-style:italic;font-weight:700;font-size:28px;color:var(--green)}
.rule{left:576px;top:1768px;width:48px;border-top:1px dotted #999}
.intro-text{left:181px;top:1798px;width:838px;text-align:center;font-size:13.5px;line-height:1.85;color:#444;letter-spacing:.3px}

/* feature rows */
.row-photo{background:linear-gradient(135deg,#f1eef3,#c9a6d1 45%,#e9a9a0 70%,#eef0ec)}
.kicker{font-size:13px;color:var(--gold-light);font-family:"Montserrat",sans-serif}
.big{font-family:"Montserrat",sans-serif;font-weight:700;font-size:36px;color:var(--gold);margin-top:6px;letter-spacing:.5px}
.row-text p{font-size:12.5px;line-height:1.72;color:#555;margin-top:12px;letter-spacing:.2px}

/* banner */
.banner{left:51px;top:2891px;width:1089px;height:203px;background:var(--banner)}
.banner .leaf{position:absolute;right:0;top:0;width:270px;height:203px;background:linear-gradient(110deg,rgba(223,226,227,0) 0%,#b9c7a3 60%,#93a97a 100%)}
.banner h2{position:absolute;left:29px;top:24px;color:#fff;font-family:"Montserrat",sans-serif;font-weight:600;font-size:17px;letter-spacing:1.5px}
.banner p{position:absolute;left:29px;top:78px;width:830px;font-size:12px;line-height:1.75;color:#666}

/* footer */
.site-footer{left:0;top:3152px;width:1200px;height:267px;background:var(--green-dark)}
.fcol{top:3195px;width:185px;font-size:10.5px;line-height:1.6;color:var(--footer-text)}
.fcol h4{font-family:"Montserrat",sans-serif;font-weight:700;font-size:10px;margin-bottom:14px;color:var(--footer-text)}
.fcol p{color:var(--footer-text)}
.fcol .in{height:30px;border:1px solid var(--footer-line);margin-top:12px;font-size:9px;color:#b8c0a8;padding:8px 10px;font-style:italic}
.fcol .sub{margin-top:10px;width:70px;height:22px;border-radius:11px;background:#fff;color:var(--green-dark);font-family:"Montserrat",sans-serif;font-size:8px;font-weight:700;text-align:center;line-height:22px}
.bottom-bar{left:0;top:3419px;width:1200px;height:69px;background:#fff}
.copy{left:198px;top:3452px;font-size:9px;color:#999;font-family:"Montserrat",sans-serif}
</style>
</head>
<body>

<header class="site-header abs">
  <svg class="abs" style="left:30px;top:36px" width="48" height="18" viewBox="0 0 48 18">
    <g fill="none" stroke="var(--green)" stroke-width="2"><path d="M0 3h4M7 3h12M0 9h4M7 9h12M0 15h4M7 15h12"/><circle cx="40" cy="5" r="4"/><path d="M33 17c1-5 13-5 14 0"/></g>
  </svg>
  <span class="nav abs caps" style="left:135px">How it works</span>
  <span class="nav abs caps" style="left:241px">Delivery areas</span>
  <span class="nav abs caps" style="left:362px">Franchise</span>
  <div class="brand abs">PetalTide<small>San Diego Flower Delivery</small></div>
  <span class="nav abs caps" style="left:738px">Blog</span>
  <span class="nav abs caps" style="left:805px">Free flowers monthly</span>
  <span class="nav abs caps" style="left:943px">Corporate arrangements</span>
  <svg class="abs" style="left:1118px;top:34px" width="66" height="22" viewBox="0 0 66 22">
    <g fill="none" stroke="var(--green)" stroke-width="2"><path d="M1 5h4l3 10h10l2-7H7"/><circle cx="10" cy="19" r="1.5"/><circle cx="17" cy="19" r="1.5"/><circle cx="55" cy="9" r="6"/><path d="M59 13l5 5"/></g>
    <circle cx="20" cy="4" r="4" fill="var(--green)"/>
  </svg>
</header>

<section class="hero abs" role="img" aria-label="Close-up photo of pink, red and white flowers on a weathered wooden table"></section>
<div class="hero-title abs">Always Fresh</div>
<div class="hero-sub abs">Beautiful Flower Arrangements Delivered Monthly</div>
<div class="hero-price abs">Now only <b>$69.95/MTH</b> ($100 value)</div>

<div class="perk abs" style="left:202px"><div class="note">For all standard order</div><div class="name">FREE VASE</div><div class="more">Read More</div></div>
<div class="perk abs" style="left:473px"><div class="note">For all standard order</div><div class="name">FREE DELIVERY</div><div class="more">Read More</div></div>
<div class="perk abs" style="left:745px"><div class="note">Only in 30 days</div><div class="name">FREE UPGRADE</div><div class="more">Read More</div></div>

<div class="card abs" style="left:77px;width:330px">
  <div class="photo" role="img" aria-label="Photo of red and white tulips in a pink glass vase" style="background:linear-gradient(160deg,#f4f4f2,#e9e4e6 50%,#e86c8d 80%,#f4f1f2)"></div>
  <div class="label">SET IT AND FORGET IT</div>
</div>
<div class="card card-feature abs" style="left:433px;width:337px">
  <div class="photo" role="img" aria-label="Photo of a hand holding a bouquet tied with string" style="background:linear-gradient(180deg,#5b5e5f,#77797a 60%,#6a6c66)"></div>
  <div class="over">BUT NEVER FORGET AGAIN</div>
  <p>When setting up your account, you can choose exact delivery dates for the months that have special days such as your Anniversary, Birthday, Valentines Day and Mothers Day. You might forget but we won't, we have got ya covered!</p>
</div>
<div class="card abs" style="left:795px;width:331px">
  <div class="photo" role="img" aria-label="Photo of purple and pink flowers in a painted teapot" style="background:linear-gradient(160deg,#f3f2f0,#d7c3dc 45%,#c89ac9 65%,#efece6)"></div>
  <div class="label">MAKING SOMEONE'S DAY BETTER</div>
</div>

<div class="signup abs">
  <h3>RECEIVE A FREE UPGRADE</h3>
  <p>Sign up to receive the coupon 10% off for your first purchase via email and get informations about flowers, accessories, tips,... and many exclusive offers.</p>
  <div class="field">Your Email...</div>
  <div class="btn">SUBSCRIBE</div>
  <div class="fine">*Discount applies only to orders over $100</div>
</div>

<div class="video abs">
  <div class="abs" style="left:30px;top:40px;width:484px;height:340px;background:#9b9ea3" role="img" aria-label="Video still introducing the subscription service"></div>
  <div class="abs" style="left:58px;top:22px;font-family:'Montserrat',sans-serif;font-size:16px;color:#fff;white-space:nowrap">Subscription Based Flower ...</div>
  <div class="abs" style="left:0;top:150px;width:544px;text-align:center;font-family:'Montserrat',sans-serif;font-size:42px;font-weight:600;color:#2b2b2b">PetalTide</div>
  <div class="abs" style="left:0;top:262px;width:544px;text-align:center;font-family:'Montserrat',sans-serif;font-size:24px;color:#222">PetalTideSD.com</div>
  <div class="abs" style="left:0;top:300px;width:544px;text-align:center;font-family:'Montserrat',sans-serif;font-size:18px;font-weight:700;color:#222;letter-spacing:2px">FILL OUT THE FORM ON OUR WEBSITE</div>
  <svg class="abs" style="left:222px;top:160px" width="100" height="100" viewBox="0 0 100 100"><circle cx="50" cy="50" r="48" fill="rgba(30,30,30,.75)"/><path d="M40 30l30 20-30 20z" fill="#fff"/></svg>
  <div class="abs" style="left:0;top:383px;width:544px;height:40px;background:#1b1b1b"></div>
  <div class="abs" style="left:0;top:380px;width:544px;height:4px;background:#d22"></div>
</div>

<h1 class="intro-title abs">Monthly Subscription Based Flower Delivery Service</h1>
<div class="rule abs"></div>
<p class="intro-text abs">Every moment of life could be cherished perfectly......If you choose wisely. To make your day more treasured, remember that flowers are the smartest choice when delivered through our monthly PetalTide subscription based delivery service. Our online subscription-based flower delivery service can help you pamper, cherish and make an everlasting impression on the minds of your loved ones with a doorstep delivery of exquisitely hand-designed floral arrangements. Our online subscription service features both standard and personalized services to help you choose from an assortment of classic and contemporary floral arrangements. It is your chance to setup a weekly, monthly, or quarterly subscription, so we can deliver the most exotic collections of hand-decorated flowers that you and your loved ones will cherish.</p>

<div class="row-photo abs" style="left:47px;top:2047px;width:546px;height:407px" role="img" aria-label="Photo of roses and lavender in a glass vase"></div>
<div class="row-text abs" style="left:646px;top:2075px;width:494px">
  <div class="kicker">Exotic Flowers Garnished With Special Hues To Compliment</div>
  <div class="big">YOUR LOVED ONES</div>
  <p>Let's not forget a single day in which you can make your loved ones feel special. Whether it's your anniversary or a birthday in your family, you must always go an extra mile to show "how much I care about you." Nothing can compare to your show of love, or compliment the joy of your loved ones, more than a perfectly blossomed bouquet of flowers. So if you are having difficulty in finding the perfect flower bouquet to share your overflowing love with that special person, don't worry......PetalTide has got it all covered for you! We believe that our hand-picked and hand-designed flowers, created with a combination of stylish designs and feminine hues, will definitely grab the attention of your loved ones. At PetalTide, we deliver both birthday flowers and sympathy flowers garnished with special hues of love and support. Our bouquets share your side of affection and sorrow with your loved ones on any memorable day of their lives.</p>
</div>

<div class="row-text abs" style="left:88px;top:2508px;width:472px">
  <div class="kicker">Standard And Personalized Flower Arrangements For</div>
  <div class="big">SPECIAL OCCASIONS</div>
  <p>PetalTide offers on time subscription based service that is risk free, trouble free and affordable at the same time. We offer the most trusted and delightful flower delivery service in San Diego, and are designed to deliver your desired floral arrangements within your requested days and times. Our local florists will happily take your orders online for your shopping convenience. You can count on us to deliver fresh flower baskets and bouquets for birthdays, weddings, mother's day, anniversaries and other special events within your locality, and even across the country. In case you're looking for something personalized, then our skilled florists can create custom arrangements for any special occasion. Get Yourself Subscribed And Claim Discounts On Big Orders!</p>
</div>
<div class="row-photo abs" style="left:593px;top:2454px;width:542px;height:407px;background:linear-gradient(135deg,#fbfbfa,#e4d5e6 45%,#c7a6cf 65%,#f3f1ec)" role="img" aria-label="Photo of pink and purple flowers in a floral teapot"></div>

<section class="banner abs">
  <div class="leaf" role="img" aria-label="Photo of a palm leaf"></div>
  <h2>GET YOURSELF SUBSCRIBED AND CLAIM DISCOUNTS ON BIG ORDERS!</h2>
  <p>Get love and adulation by gifting flowers to your loved ones on those special occasions. Whether it's formal, personal or your love for your family, just follow the subscription criteria and get your hands on the most valuable service for all kinds of events, occasions and parties. Set up your account and select the right delivery dates for the special months and leave the rest to us. We will deliver your flowers on the exact special dates to make your loved one's day wonderful. It is your chance to experience the simple, risk-free and trouble-free delivery of flowers right to the doorstep of your cherished loved</p>
</section>

<footer class="site-footer abs"></footer>
<div class="fcol abs" style="left:198px">
  <h4>ABOUT US</h4>
  <p>Lorem ipsum dolor sit amet, consectetur adipiscing elit. Sed do eiusmod tempor incididunt ut labore et dolore magna aliqua.</p>
  <p style="margin-top:8px">Ut enim ad minim veniam, quis nostrud exercitation ullamco.</p>
</div>
<div class="fcol abs" style="left:400px">
  <h4>INFORMATION</h4>
  <p>Corporate Arrangements<br>Hotel Arrangements<br>Events<br>Weddings</p>
</div>
<div class="fcol abs" style="left:605px">
  <h4>RECEIVE A FREE UPGRADE</h4>
  <p>Enter your email and we'll send you a coupon with 10% off your next order.</p>
  <div class="in">Your Email...</div>
  <div class="sub">SUBMIT</div>
</div>
<div class="fcol abs" style="left:810px">
  <h4>CONTACT US</h4>
  <p style="font-style:italic">418 Harbor Lane,<br>Bayview CA 90000</p>
  <p style="margin-top:8px">Phone: 555-014-2230</p>
  <p style="margin-top:8px">Email: hello@petaltide.com</p>
  <svg style="margin-top:14px" width="140" height="26" viewBox="0 0 140 26">
    <circle cx="13" cy="13" r="12" fill="#fff"/>
    <g fill="none" stroke="var(--footer-line)" stroke-width="1.5"><circle cx="44" cy="13" r="11"/><circle cx="73" cy="13" r="11"/><circle cx="102" cy="13" r="11"/><circle cx="131" cy="13" r="8.5"/></g>
  </svg>
</div>

<div class="bottom-bar abs"></div>
<div class="copy abs">© COPYRIGHT 2016. ALL RIGHTS RESERVED.</div>
<svg class="abs" style="left:852px;top:3442px" width="220" height="20" viewBox="0 0 220 20">
  <g fill="#c9c9c9"><rect x="0" y="3" width="26" height="15" rx="2"/><rect x="32" y="3" width="26" height="15" rx="2"/><rect x="64" y="3" width="26" height="15" rx="2"/><rect x="96" y="3" width="26" height="15" rx="2"/><rect x="128" y="3" width="26" height="15" rx="2"/><rect x="160" y="3" width="26" height="15" rx="2"/><rect x="192" y="3" width="26" height="15" rx="2"/></g>
</svg>
<svg class="abs" style="left:1090px;top:3438px" width="28" height="28" viewBox="0 0 28 28"><circle cx="14" cy="14" r="13" fill="#cfcfcf"/><path d="M9 16l5-5 5 5" fill="none" stroke="#fff" stroke-width="2"/></svg>

</body>
</html>
```